Employee Portal UI Design - Modern and Clean

We are an agency tasked with developing a team portal for a company that has many employees. As we embark on this project, we seek a great UI design to accompany the requirements our client has for this project. We already have several screens mocked up that can be used as reference for the overall idea. Currently, we are only looking for the main dashboard's home page, user registration screen, and account settings page to be designed. The main brand colors are red but other accents can be used as well. The client's vision is for modern & minimalist to be at the center. We have a specific font to be used, but if you don't have access to it, you can just use a similar font.Main color: #DD0031The sub menus (do not need to be designed) would be:>Performance Reviews>Posts>Team directory>Calendar>Tasks>Documents>LinksWe would prefer the design be made in Adobe XD.

Industry/Entity Type

Fast Food Restaurant

Number of Pages Required

1 page

Font styles to use
Sans Serif

Colors
ec1f27

Requirements
Must have
• Color: #DD0031 (highlights)

```html
<!DOCTYPE html>
<html lang="en">
<head>
<meta charset="utf-8">
<title>Team Portal – Dashboard Home</title>
<link href="https://fonts.googleapis.com/css2?family=Carlito:wght@400;700&family=Open+Sans:wght@300;400&display=swap" rel="stylesheet">
<style>
  :root {
    --brand-red: #cf0a3c;
    --blue: #1a6fd6;
    --band: #cccccc;
    --card: #ffffff;
    --border: #b9b9b9;
    --divider: #c4c4c4;
    --ink: #222222;
    --heading: #333333;
    --muted: #8a8a8a;
    --section: #666666;
    --avatar: #9a9a9a;
  }
  * { box-sizing: border-box; margin: 0; padding: 0; }
  html, body { width: 1200px; height: 1000px; overflow: hidden; background: #fff; }
  body { font-family: "Carlito", "Calibri", sans-serif; color: var(--ink); position: relative; }

  .dashboard { position: absolute; left: 0; top: 125px; width: 1200px; height: 750px; background: var(--band); }
  .abs { position: absolute; }

  .panel-title { position: absolute; font-family: "Open Sans", sans-serif; font-weight: 300; font-size: 33px; color: var(--heading); text-align: center; line-height: 1; }

  .search { left: 30px; top: 66px; width: 790px; height: 30px; background: var(--card); border: 1px solid var(--border); border-radius: 3px; display: flex; align-items: center; padding-left: 10px; gap: 7px; font-size: 13px; color: var(--muted); }

  .day-label { position: absolute; left: 62px; width: 758px; text-align: center; font-size: 23px; color: var(--section); line-height: 1; }

  .post { position: absolute; left: 62px; width: 758px; background: var(--card); border: 1px solid var(--border); border-radius: 3px; }
  .avatar { position: absolute; left: -32px; width: 64px; height: 64px; border-radius: 50%; background: var(--avatar); }
  .post-title { position: absolute; left: 42px; top: 6px; font-size: 20px; font-weight: 700; color: var(--heading); white-space: nowrap; }
  .post-title .author { color: var(--brand-red); }
  .post-body { position: absolute; left: 42px; top: 35px; width: 530px; font-size: 14.6px; line-height: 17.5px; color: var(--ink); }
  .post-meta { position: absolute; right: 10px; top: 10px; text-align: right; font-size: 12px; color: var(--muted); line-height: 15px; }
  .meta-row { display: flex; justify-content: flex-end; align-items: center; gap: 4px; margin-bottom: 5px; }
  .meta-row.tight { margin-bottom: 0; }
  .audience { color: var(--brand-red); font-size: 11.5px; margin-top: -3px; }

  .fab { position: absolute; left: 715px; top: 616px; width: 94px; height: 94px; border-radius: 50%; background: var(--brand-red); }

  .widget { position: absolute; left: 850px; width: 320px; background: var(--card); border: 1px solid var(--border); border-radius: 3px; }
  .row { display: flex; align-items: center; border-bottom: 1px solid var(--divider); }
  .view-all { display: flex; align-items: center; justify-content: center; color: var(--brand-red); font-size: 16px; height: 40px; }

  .event { height: 41px; padding-left: 12px; }
  .event .day { font-size: 23px; font-weight: 700; width: 30px; margin-left: 10px; color: var(--heading); }
  .event .date-stack { font-size: 11px; line-height: 10px; width: 62px; color: var(--heading); }
  .event .date-stack b { display: block; font-size: 12px; }
  .event .event-name { font-size: 17px; line-height: 15px; color: var(--heading); }
  .event .event-info { font-size: 8.5px; color: var(--muted); line-height: 10px; }

  .task-group { height: 31px; text-align: right; padding: 10px 4px 0 0; font-size: 15px; color: var(--muted); border-bottom: 1px solid var(--divider); }
  .task { height: 41px; padding-left: 12px; font-size: 18px; color: var(--heading); }
  .task .time { width: 91px; margin-left: 10px; }
  .task .time b { font-weight: 700; }

  .poll-question { text-align: center; font-size: 14px; color: var(--ink); padding-top: 8px; height: 33px; }
  .poll-option { margin: 0 29px 4px 29px; height: 32px; border: 1px solid #d8d8d8; border-radius: 3px; display: flex; align-items: center; justify-content: space-between; padding: 0 10px; font-size: 12px; color: var(--ink); }
  .vote-btn { display: block; margin: 4px auto 0; width: 100px; height: 23px; background: var(--brand-red); color: #fff; font-size: 12px; border-radius: 2px; text-align: center; line-height: 23px; }
  .poll-foot { border-top: 1px solid var(--divider); margin-top: 5px; height: 41px; }
</style>
</head>
<body>
<main class="dashboard">

  <!-- Recent activities -->
  <h1 class="panel-title" style="left:62px; width:656px; top:25px;">Recent Activities</h1>
  <div class="abs search">
    <svg width="17" height="17" viewBox="0 0 17 17"><circle cx="7" cy="7" r="5.5" fill="none" stroke="#999" stroke-width="1.6"/><line x1="11" y1="11" x2="16" y2="16" stroke="#999" stroke-width="1.8"/></svg>
    44 posts
  </div>

  <svg width="0" height="0" style="position:absolute">
    <defs>
      <symbol id="user" viewBox="0 0 64 64"><circle cx="32" cy="21" r="10" fill="none" stroke="#fff" stroke-width="2.2"/><path d="M14 52c0-11 8-16 18-16s18 5 18 16z" fill="none" stroke="#fff" stroke-width="2.2" stroke-linejoin="round"/></symbol>
      <symbol id="clock" viewBox="0 0 16 16"><circle cx="8" cy="8" r="6.8" fill="none" stroke="#8a8a8a" stroke-width="1.4"/><path d="M8 4v4h3" fill="none" stroke="#8a8a8a" stroke-width="1.4"/></symbol>
      <symbol id="eye" viewBox="0 0 24 16"><path d="M1 8c3-5 7-7 11-7s8 2 11 7c-3 5-7 7-11 7S4 13 1 8z" fill="none" stroke="#8a8a8a" stroke-width="1.5"/><circle cx="12" cy="8" r="3.5" fill="none" stroke="#8a8a8a" stroke-width="1.5"/></symbol>
      <symbol id="eye-off" viewBox="0 0 24 18"><path d="M1 9c3-5 7-7 11-7s8 2 11 7c-3 5-7 7-11 7S4 14 1 9z" fill="none" stroke="#8a8a8a" stroke-width="1.5"/><circle cx="12" cy="9" r="3.5" fill="none" stroke="#8a8a8a" stroke-width="1.5"/><line x1="4" y1="17" x2="21" y2="1" stroke="#8a8a8a" stroke-width="1.5"/></symbol>
    </defs>
  </svg>

  <div class="day-label" style="top:105px;">Today</div>

  <article class="post" style="top:133px; height:151px;">
    <svg class="avatar" style="top:7px;"><use href="#user"/></svg>
    <h2 class="post-title"><span class="author">Marcus Bell</span> - Post Subject</h2>
    <p class="post-body">Lorem ipsum dolor sit amet, consectetur adipisicing elit, sed do eiusmod tempor incididunt ut labore et dolore magna aliqua. Ut enim ad minim veniam, quis nostrud exercitation ullamco laboris nisi ut aliquip ex ea commodo consequat. Duis aute irure dolor in reprehenderit in voluptate velit esse cillum dolore eu fugiat nulla pariatur. Excepteur sint occaecat cupidatat non proident, sunt in culpa qui officia deserunt mollit anim id est laborum. Sed ut perspiciatis unde omnis iste natus error sit voluptatem...</p>
    <div class="post-meta">
      <div class="meta-row">01:43 AM <svg width="16" height="16"><use href="#clock"/></svg></div>
      <div class="meta-row">Public <svg width="24" height="16"><use href="#eye"/></svg></div>
    </div>
  </article>

  <article class="post" style="top:289px; height:81px;">
    <svg class="avatar" style="top:4px;"><use href="#user"/></svg>
    <h2 class="post-title"><span class="author">Marcus Bell</span> - Post Subject</h2>
    <p class="post-body">Lorem ipsum dolor sit amet, consectetur adipisicing elit, sed do eiusmod tempor incididunt ut labore et dolore magna aliqua. Ut enim ad minim veniam, quis nostrud...</p>
    <div class="post-meta">
      <div class="meta-row">01:43 AM <svg width="16" height="16"><use href="#clock"/></svg></div>
      <div class="meta-row tight">Private <svg width="24" height="18"><use href="#eye-off"/></svg></div>
      <div class="audience">Team Leaders</div>
    </div>
  </article>

  <div class="day-label" style="top:378px;">Yesterday</div>

  <article class="post" style="top:407px; height:101px;">
    <svg class="avatar" style="top:4px;"><use href="#user"/></svg>
    <h2 class="post-title"><span class="author">New Perfomance Review</span> - Performance review for Marcus Be...</h2>
    <p class="post-body" style="top:31px;">Lorem ipsum dolor sit amet, consectetur adipisicing elit, sed do eiusmod tempor incididunt ut labore et dolore magna aliqua. Ut enim ad minim veniam, quis nostrud exercitation ullamco laboris nisi ut aliquip ex ea commodo consequat. Duis aute irure...</p>
    <div class="post-meta">
      <div class="meta-row tight">Saturday, March 2 <svg width="16" height="16"><use href="#clock"/></svg></div>
      <div class="meta-row" style="padding-right:20px;">01:43 AM</div>
      <div class="meta-row">Public <svg width="24" height="16"><use href="#eye"/></svg></div>
    </div>
  </article>

  <div class="day-label" style="top:516px;">Earlier</div>

  <article class="post" style="top:545px; height:176px;">
    <svg class="avatar" style="top:4px;"><use href="#user"/></svg>
    <h2 class="post-title"><span class="author">Marcus Bell</span> - Post Subject</h2>
    <p class="post-body">Lorem ipsum dolor sit amet, consectetur adipisicing elit, sed do eiusmod tempor incididunt ut labore et dolore magna aliqua. Ut enim ad minim veniam, quis nostrud exercitation ullamco laboris nisi ut aliquip ex ea commodo consequat. Duis aute irure dolor in reprehenderit in voluptate velit esse cillum dolore eu fugiat nulla pariatur. Excepteur sint occaecat cupidatat non proident, sunt in culpa qui officia deserunt mollit anim id est laborum. Sed ut perspiciatis unde omnis iste natus error sit voluptatem accusantium doloremque laudantium, totam rem aperiam, eaque ipsa quae ab illo...</p>
    <div class="post-meta">
      <div class="meta-row tight">Monday, February 25 <svg width="16" height="16"><use href="#clock"/></svg></div>
      <div class="meta-row" style="padding-right:20px;">01:43 AM</div>
      <div class="meta-row">Public <svg width="24" height="16"><use href="#eye"/></svg></div>
    </div>
  </article>

  <svg class="fab" viewBox="0 0 94 94" aria-label="New post"><path d="M47 25v44M25 47h44" stroke="#fff" stroke-width="7" stroke-linecap="round"/></svg>

  <!-- Events -->
  <h2 class="panel-title" style="left:850px; width:320px; top:26px;">Events</h2>
  <section class="widget" style="top:65px;">
    <div class="row event">
      <svg width="14" height="16"><path d="M2 1v15" stroke="var(--brand-red)" stroke-width="2"/><path d="M3 2h10l-3 4 3 4H3z" fill="var(--brand-red)"/></svg>
      <span class="day">18</span><span class="date-stack"><b>JAN</b>Thursday</span>
      <div><div class="event-name">Director Meeting</div><div class="event-info">Restaurant|10:00 am - 11:00 am</div></div>
    </div>
    <div class="row event">
      <svg width="14" height="16"><path d="M2 1v15" stroke="var(--blue)" stroke-width="2"/><path d="M3 2h10l-3 4 3 4H3z" fill="var(--blue)"/></svg>
      <span class="day">20</span><span class="date-stack"><b>JAN</b>Saturday</span>
      <div><div class="event-name">Free Breakfast</div><div class="event-info">Restaurant|06:30 am - 10:30 am</div></div>
    </div>
    <div class="row event">
      <svg width="14" height="16"><path d="M2 1v15" stroke="var(--blue)" stroke-width="2"/><path d="M3 2h10l-3 4 3 4H3z" fill="var(--blue)"/></svg>
      <span class="day">23</span><span class="date-stack"><b>JAN</b>Tuesday</span>
      <div><div class="event-name">Daddy Daughter Night</div><div class="event-info">Restaurant|06:00 pm - 08:00 pm</div></div>
    </div>
    <div class="view-all">View All Events</div>
  </section>

  <!-- Tasks -->
  <h2 class="panel-title" style="left:850px; width:320px; top:236px;">Tasks</h2>
  <section class="widget" style="top:275px;">
    <div class="task-group">Tomorrow</div>
    <div class="row task">
      <svg width="16" height="16"><circle cx="8" cy="8" r="7.5" fill="var(--brand-red)"/><path d="M8 3.5v5.5" stroke="#fff" stroke-width="2"/><circle cx="8" cy="11.8" r="1.2" fill="#fff"/></svg>
      <span class="time"><b>08:45</b> pm</span>Daily Safe Checklist
    </div>
    <div class="row task">
      <svg width="16" height="16"><circle cx="8" cy="8" r="7.5" fill="var(--blue)"/><path d="M8 3.5v5.5" stroke="#fff" stroke-width="2"/><circle cx="8" cy="11.8" r="1.2" fill="#fff"/></svg>
      <span class="time"><b>09:15</b> pm</span>Daily eRQA
    </div>
    <div class="task-group">Friday</div>
    <div class="row task">
      <svg width="16" height="16"><circle cx="8" cy="8" r="7.5" fill="var(--brand-red)"/><path d="M8 3.5v5.5" stroke="#fff" stroke-width="2"/><circle cx="8" cy="11.8" r="1.2" fill="#fff"/></svg>
      <span class="time"><b>08:45</b> pm</span>Daily Safe Checklist
    </div>
    <div class="view-all">View All Tasks</div>
  </section>

  <!-- Polls -->
  <h2 class="panel-title" style="left:850px; width:320px; top:509px;">Polls</h2>
  <section class="widget" style="top:547px;">
    <div class="poll-question">What is your favorite entree?</div>
    <div class="poll-option">Crispy Hen Sandwitch
      <svg width="18" height="16"><path d="M2 8l5 5 9-11" fill="none" stroke="var(--brand-red)" stroke-width="2.8"/></svg>
    </div>
    <div class="poll-option">Chicken Strips</div>
    <span class="vote-btn">Submit Vote</span>
    <div class="poll-foot view-all">View All Polls</div>
  </section>

</main>
</body>
</html>
```